We need flyer to promote our new FMLA / Disability Form Completion Service.
CareVista is a Health Data Services company supporting Hospitals and Medical Practices in the secure electronic exchange, delivery and integration of protected health information (PHI). CareVista Services include Release of Information, Audit and Chart Review, Disability and Family and Medical Leave Act (FMLA) form processing, and revenue cycle support services.

I have attached some of the other collateral we have for our other service lines. We would like for the colour/imagery to somewhat coordinate with these.

For further reference about the company : www.carevista-partners.example

The flyer we are hoping to receive is specific to the Disability and FMLA Form Processing (in Bold above). I’ve attached a copy of our workflow for your review. The value delivered to the client as a result of engaging this service is as follows:

-Reduce internal labor costs
-Improve quality
-Accelerate turnaround time
-Improve patient satisfaction
-Reduce internal phone traffic

CareVista manages all aspects of the FMLA form completion process including:

-Review for HIPAA compliance
-Completion of forms
-Communication with patient/requesting parties
-Signing off on forms (as approved by the client)
-Invoicing
Delivery
Tracking/Reporting

CareVista clients are provided complete transparency into all CareVista actions and documents for tracking and accountability purposes.

Target Market(s)

CareVista’s target market are Hospital Executives and Health Information Management Directors and Medical Practice Administrators.

Requirements
Must have
• Outline value of FMLA/Disability Form Completion Service:
• The value delivered to the client as a result of engaging this service is as follows:
• • Reduce internal labor costs
• • Improve quality
• • Accelerate turnaround time
• • Improve patient satisfaction
• • Reduce internal phone traffic
• CareVista manages all aspects of the FMLA form completion process including:
• • Review for HIPAA compliance
• • Completion of forms
• • Communication with patient/requesting parties
• • Signing off on forms (as approved by client)
• • Invoicing
• • Delivery
• • Tracking/Reporting
• CareVista clients are provided complete transparency into all CareVista actions and documents for tracking and accountability purposes.
Nice to have
• Similar imagery/colors as the current marketing materials being used on our website and the materials uploaded to this project.

```html
<!DOCTYPE html>
<html lang="en">
<head>
<meta charset="utf-8">
<title>CareVista Group – FMLA / Disability Form Completion</title>
<link rel="stylesheet" href="https://fonts.googleapis.com/css2?family=Open+Sans:wght@400;600;700&display=swap">
<style>
  :root {
    --green: #6cb33f;
    --green-dark: #5a9c33;
    --blue: #1f88c9;
    --text: #555b60;
    --grey: #8a8f93;
    --paper: #ffffff;
    --photo-light: #dfe7ee;
    --photo-mid: #b9c7d3;
    --photo-warm: #c9b8a6;
  }
  * { box-sizing: border-box; margin: 0; padding: 0; }
  html, body { width: 900px; height: 1200px; overflow: hidden; }
  body {
    font-family: "Open Sans", Arial, sans-serif;
    background: var(--paper);
    color: var(--text);
  }
  .flyer { position: relative; width: 900px; height: 1200px; overflow: hidden; }

  .header {
    height: 160px;
    display: flex;
    justify-content: space-between;
    align-items: center;
    padding: 0 50px;
  }
  .brand {
    display: flex; align-items: center; gap: 14px;
    font-size: 44px; font-weight: 700; color: var(--green);
    letter-spacing: -0.5px;
  }
  .brand-dot { width: 22px; height: 22px; border-radius: 50%; background: var(--green); }
  .contact { text-align: right; font-size: 17px; color: var(--text); }
  .contact-line { display: flex; align-items: center; justify-content: flex-end; gap: 10px; margin: 8px 0; }
  .contact-line svg { width: 22px; height: 22px; }

  .hero {
    height: 350px;
    background: linear-gradient(120deg, var(--photo-light) 0%, var(--photo-mid) 55%, var(--photo-warm) 100%);
  }

  .main {
    display: flex;
    gap: 28px;
    padding: 26px 50px 0 50px;
  }
  .left { width: 395px; }
  .right { flex: 1; }

  .title {
    font-size: 23px; font-weight: 700; color: var(--blue);
    text-transform: uppercase; letter-spacing: 0.2px;
    margin-bottom: 14px;
  }
  .section-head { font-size: 18px; font-weight: 700; color: var(--blue); margin-bottom: 8px; }
  .about p { font-size: 12.5px; line-height: 1.55; margin-bottom: 10px; }
  .value-head {
    font-size: 19px; font-weight: 700; color: var(--blue);
    line-height: 1.3; margin: 16px 0 10px;
  }

  .checklist { list-style: none; }
  .checklist li {
    display: flex; align-items: center; gap: 10px;
    font-size: 15px; line-height: 1.35; padding: 4px 0;
  }
  .checklist svg { width: 14px; height: 14px; flex: none; }

  .thumbs { display: flex; gap: 10px; margin-top: 20px; }
  .thumb {
    flex: 1; height: 110px;
    background: linear-gradient(135deg, var(--photo-light), var(--photo-mid));
  }
  .thumb:nth-child(2) { background: linear-gradient(135deg, var(--photo-mid), var(--photo-warm)); }

  .care-photo {
    height: 210px;
    background: linear-gradient(135deg, #e7dccf 0%, var(--photo-mid) 60%, #9fb3c4 100%);
  }
  .process {
    background: var(--green);
    color: #fff;
    padding: 20px 24px 22px;
  }
  .process-head { font-size: 18px; font-weight: 700; line-height: 1.35; margin-bottom: 10px; }
  .process .checklist li { font-size: 14px; padding: 3px 0; }
  .transparency {
    font-size: 13px; line-height: 1.45;
    margin-top: 12px; padding-top: 10px;
    border-top: 1px solid rgba(255,255,255,0.5);
  }

  .footer-bar {
    position: absolute; left: 0; right: 0; bottom: 0;
    height: 22px; background: var(--green);
  }
</style>
</head>
<body>
<div class="flyer">
  <header class="header">
    <div class="brand"><span class="brand-dot"></span>CareVista Group</div>
    <div class="contact">
      <div class="contact-line">800.555.0142
        <svg viewBox="0 0 22 22"><circle cx="11" cy="11" r="11" fill="var(--green)"/><path d="M7.5 6.5c.6-.6 1.4-.5 1.8.1l.9 1.5c.3.5.2 1.1-.2 1.5l-.6.5c.5 1.1 1.4 2 2.5 2.5l.5-.6c.4-.4 1-.5 1.5-.2l1.5.9c.6.4.7 1.2.1 1.8l-.7.7c-3.4.6-7.6-3.6-7-7z" fill="#fff"/></svg>
      </div>
      <div class="contact-line">www.carevista-partners.example
        <svg viewBox="0 0 22 22"><circle cx="11" cy="11" r="11" fill="var(--green)"/><path d="M9 7l4 4-4 4" stroke="#fff" stroke-width="2" fill="none" stroke-linecap="round" stroke-linejoin="round"/></svg>
      </div>
    </div>
  </header>

  <div class="hero" role="img" aria-label="Photo of a doctor shaking hands with a patient in a clinic office"></div>

  <main class="main">
    <section class="left">
      <h1 class="title">FMLA / Disability Form Completion</h1>
      <div class="about">
        <h2 class="section-head">About CareVista Group</h2>
        <p>CareVista Group is a Health Data Services company supporting Hospitals and Medical Practices in the secure electronic exchange, delivery and integration of protected health information (PHI).</p>
        <p>CareVista services include Release of Information, Audit and Chart Review, Disability and Family and Medical Leave Act (FMLA) form processing, and revenue cycle support services.</p>
      </div>
      <h2 class="value-head">The value delivered to the client as a result of engaging this service is as follows:</h2>
      <ul class="checklist value-list">
        <li><svg viewBox="0 0 14 14"><path d="M1.5 7.5l3.5 3.5 7.5-8" stroke="var(--green)" stroke-width="2.4" fill="none" stroke-linecap="round" stroke-linejoin="round"/></svg>Reduce internal labor costs</li>
        <li><svg viewBox="0 0 14 14"><path d="M1.5 7.5l3.5 3.5 7.5-8" stroke="var(--green)" stroke-width="2.4" fill="none" stroke-linecap="round" stroke-linejoin="round"/></svg>Accelerate turnaround time</li>
        <li><svg viewBox="0 0 14 14"><path d="M1.5 7.5l3.5 3.5 7.5-8" stroke="var(--green)" stroke-width="2.4" fill="none" stroke-linecap="round" stroke-linejoin="round"/></svg>Improve patient satisfaction</li>
        <li><svg viewBox="0 0 14 14"><path d="M1.5 7.5l3.5 3.5 7.5-8" stroke="var(--green)" stroke-width="2.4" fill="none" stroke-linecap="round" stroke-linejoin="round"/></svg>Reduce internal phone traffic</li>
        <li><svg viewBox="0 0 14 14"><path d="M1.5 7.5l3.5 3.5 7.5-8" stroke="var(--green)" stroke-width="2.4" fill="none" stroke-linecap="round" stroke-linejoin="round"/></svg>Improve quality</li>
      </ul>
      <div class="thumbs">
        <div class="thumb" role="img" aria-label="Photo of medical staff in a hospital corridor"></div>
        <div class="thumb" role="img" aria-label="Photo of a doctor consulting with a patient"></div>
        <div class="thumb" role="img" aria-label="Photo of healthcare professionals reviewing records"></div>
      </div>
    </section>

    <section class="right">
      <div class="care-photo" role="img" aria-label="Photo of a nurse talking with an elderly couple"></div>
      <div class="process">
        <h2 class="process-head">CareVista manages all aspects of the FMLA form completion process including:</h2>
        <ul class="checklist">
          <li><svg viewBox="0 0 14 14"><path d="M1.5 7.5l3.5 3.5 7.5-8" stroke="#fff" stroke-width="2.4" fill="none" stroke-linecap="round" stroke-linejoin="round"/></svg>Review for HIPAA compliance</li>
          <li><svg viewBox="0 0 14 14"><path d="M1.5 7.5l3.5 3.5 7.5-8" stroke="#fff" stroke-width="2.4" fill="none" stroke-linecap="round" stroke-linejoin="round"/></svg>Completion of forms</li>
          <li><svg viewBox="0 0 14 14"><path d="M1.5 7.5l3.5 3.5 7.5-8" stroke="#fff" stroke-width="2.4" fill="none" stroke-linecap="round" stroke-linejoin="round"/></svg>Communication with patient/requesting parties</li>
          <li><svg viewBox="0 0 14 14"><path d="M1.5 7.5l3.5 3.5 7.5-8" stroke="#fff" stroke-width="2.4" fill="none" stroke-linecap="round" stroke-linejoin="round"/></svg>Signing off on forms (as approved by the client)</li>
          <li><svg viewBox="0 0 14 14"><path d="M1.5 7.5l3.5 3.5 7.5-8" stroke="#fff" stroke-width="2.4" fill="none" stroke-linecap="round" stroke-linejoin="round"/></svg>Tracking/Reporting</li>
          <li><svg viewBox="0 0 14 14"><path d="M1.5 7.5l3.5 3.5 7.5-8" stroke="#fff" stroke-width="2.4" fill="none" stroke-linecap="round" stroke-linejoin="round"/></svg>Invoicing</li>
          <li><svg viewBox="0 0 14 14"><path d="M1.5 7.5l3.5 3.5 7.5-8" stroke="#fff" stroke-width="2.4" fill="none" stroke-linecap="round" stroke-linejoin="round"/></svg>Delivery</li>
        </ul>
        <p class="transparency">CareVista clients are provided complete transparency into all CareVista actions and documents for tracking and accountability purposes.</p>
      </div>
    </section>
  </main>

  <div class="footer-bar"></div>
</div>
</body>
</html>
```